Online interactive tutorial for year 2 to year 12 students in Australia

Website design for a new online tutorial for year 2 to year 12 students in Australia.

- The tutorial will be conducted via live webcam and within a dedicated interactive space
- The tutorial will be provided by high scoring undergraduates studying in top Australian universities.
- The tutors will be going through interviews & assessments & only top students are allowed to apply.
- Parents will do search and select tutor and have short 15 mins video interaction with potential tutors before booking them for their children for tutoring.
- hourly cost of booking (no monthly subscription or no hour limits)
- Tutors will have their own profile

Please see the attached for detailed page functionality.

The look and feel of the design must consider the following:
- must be educational but not dull and should stand out
- must appeal to younger generation - tutees (8-18 years), tutors (19-25), parents (30-50).
- Ideas for Logos (brivano.com.au but not confirmed)

Target Market(s)

tutees (8-18 years), tutors (19-25 years), parents (30-50 years).

Industry/Entity Type

Education

Coding

Coded - Design and coding required

Number of Pages Required

5+ page

Font styles to use
Serif

Requirements
Must have
• The look and feel of the design must consider the following:
• - must be educational but not dull and should stand out
• - must appeal to younger generation - tutees (8-18 years), tutors (19-25), parents (30-50).
Should not have
• Dullness

```html
<!DOCTYPE html>
<html lang="en">
<head>
<meta charset="utf-8">
<title>Brivano – Parent's Registration</title>
<link rel="stylesheet" href="https://fonts.googleapis.com/css2?family=Open+Sans:wght@400;600;700&family=Roboto:wght@400;500&family=Roboto+Condensed:wght@700&display=swap">
<style>
:root{
  --blue:#2a7cc4;
  --blue-dark:#1f6fb2;
  --cyan:#1ba0dc;
  --footer:#333333;
  --footer-bar:#00a0d6;
  --text:#444;
  --field-bg:#f6f6f6;
  --field-border:#dedede;
  --white:#fff;
}
*{box-sizing:border-box;margin:0;padding:0}
html,body{width:1200px;height:1200px;overflow:hidden;background:var(--white);font-family:'Open Sans',sans-serif;color:var(--text)}
.page{position:relative;width:1200px;height:1200px}

/* header */
.site-header{position:absolute;top:0;left:0;width:1200px;height:116px}
.brand{position:absolute;left:99px;top:28px;display:flex;align-items:center;gap:10px}
.brand-dot{width:36px;height:36px;border-radius:50%;background:var(--cyan)}
.brand-name{font-size:37px;font-weight:700;color:#4a4a4a;letter-spacing:.5px}
.search{position:absolute;left:363px;top:37px;width:360px;height:34px;border:1px solid #ccc;border-radius:3px;display:flex;background:#fff}
.search-field{flex:1;font-size:12px;padding:0 14px;line-height:32px;position:relative}
.search-field::after{content:"";position:absolute;right:12px;top:14px;border:4px solid transparent;border-top:5px solid #666}
.search-btn{width:38px;background:#e9e9e9;border-left:1px solid #ccc;display:flex;align-items:center;justify-content:center}
.role-btn{position:absolute;top:38px;height:34px;border:2px solid var(--blue);border-radius:2px;color:var(--blue);font-size:13px;display:flex;align-items:center;justify-content:center;gap:6px}
.login-btn{position:absolute;left:1032px;top:38px;width:69px;height:34px;background:var(--blue);border-radius:3px;color:#fff;font-family:'Roboto',sans-serif;font-size:14px;display:flex;align-items:center;justify-content:center}

/* nav */
.main-nav{position:absolute;top:116px;left:0;width:1200px;height:49px;background:var(--blue)}
.main-nav a{position:absolute;top:0;height:49px;line-height:49px;color:#fff;font-family:'Roboto',sans-serif;font-size:13.5px;text-decoration:none;text-align:center}
.main-nav .divider{position:absolute;top:0;width:1px;height:49px;background:rgba(0,0,0,.15)}

/* hero */
.hero{position:absolute;top:165px;left:0;width:1200px;height:330px}
.hero svg{position:absolute;top:0;left:0}
.hero-title{position:absolute;top:150px;width:1200px;text-align:center;font-family:'Roboto Condensed',sans-serif;font-weight:700;font-size:44px;color:#fff;letter-spacing:.5px}

/* form */
.field{position:absolute;width:368px;height:38px;background:var(--field-bg);border:1px solid var(--field-border);font-size:11.5px;padding:0 15px;line-height:36px;color:#555}
.field .hint{color:#aaa;margin-left:4px}
.field.add-child{background:linear-gradient(#f8f8f8,#e9e9e9);text-align:center;text-transform:uppercase}
.register-btn{position:absolute;left:551px;top:773px;width:99px;height:32px;background:var(--blue);border-radius:3px;color:#fff;font-family:'Roboto',sans-serif;font-size:17px;display:flex;align-items:center;justify-content:center}

/* footer */
.site-footer{position:absolute;top:858px;left:0;width:1200px;height:291px;background:var(--footer);color:#fff}
.footer-heading{position:absolute;top:36px;font-family:'Roboto',sans-serif;font-size:17.5px;font-weight:400;text-transform:uppercase}
.footer-text{position:absolute;font-size:13px;line-height:20px}
.contact-icon{position:absolute}
.links{position:absolute;left:425px;top:82px;list-style:none;font-size:13.5px;line-height:21.5px}
.links li{padding-left:18px;position:relative}
.links li::before{content:"";position:absolute;left:2px;top:7px;border:4px solid transparent;border-left:5px solid #fff;border-right:0}
.news-text{position:absolute;left:623px;top:73px;width:305px;font-size:11.5px;line-height:19px}
.news-input{position:absolute;left:624px;top:124px;width:293px;height:41px;background:#fff;color:#555;font-size:11.5px;padding-left:14px;line-height:41px}
.news-btn{position:absolute;left:623px;top:175px;width:102px;height:41px;background:var(--footer-bar);font-family:'Roboto',sans-serif;font-size:14px;display:flex;align-items:center;justify-content:center;text-transform:uppercase}
.social{position:absolute;left:1006px;top:80px;list-style:none}
.social li{display:flex;align-items:center;gap:10px;height:26px;margin-bottom:10.5px;font-size:15px}
.social .ring{width:26px;height:26px;border:1.5px solid #fff;border-radius:50%}
.copyright{position:absolute;top:1149px;left:0;width:1200px;height:51px;background:var(--footer-bar);color:#fff;font-size:12.5px;text-align:center;line-height:51px}
</style>
</head>
<body>
<div class="page">

<header class="site-header">
  <div class="brand"><span class="brand-dot"></span><span class="brand-name">Brivano</span></div>
  <div class="search">
    <div class="search-field">Search</div>
    <div class="search-btn">
      <svg width="13" height="13" viewBox="0 0 13 13"><circle cx="5.5" cy="5.5" r="4" fill="none" stroke="#333" stroke-width="1.8"/><line x1="8.5" y1="8.5" x2="12" y2="12" stroke="#333" stroke-width="2"/></svg>
    </div>
  </div>
  <div class="role-btn" style="left:745px;width:77px">
    <svg width="13" height="14" viewBox="0 0 13 14"><circle cx="6.5" cy="4" r="3.3" fill="#2a7cc4"/><path d="M0.5 14c0-4 2.7-5.8 6-5.8s6 1.8 6 5.8z" fill="#2a7cc4"/></svg>Tutor</div>
  <div class="role-btn" style="left:833px;width:82px">
    <svg width="14" height="14" viewBox="0 0 14 14"><circle cx="4" cy="3" r="2.3" fill="#2a7cc4"/><circle cx="10" cy="3" r="2.3" fill="#2a7cc4"/><rect x="1.5" y="6" width="5" height="8" rx="1.5" fill="#2a7cc4"/><rect x="7.5" y="6" width="5" height="8" rx="1.5" fill="#2a7cc4"/></svg>Parent</div>
  <div class="role-btn" style="left:928px;width:92px">
    <svg width="15" height="14" viewBox="0 0 15 14"><path d="M1 3l6.5-2.5L14 3 7.5 5.5z" fill="#2a7cc4"/><circle cx="7.5" cy="6" r="2.6" fill="#2a7cc4"/><path d="M2 14c0-3.5 2.5-5 5.5-5s5.5 1.5 5.5 5z" fill="#2a7cc4"/></svg>Tutees</div>
  <div class="login-btn">LOGIN</div>
</header>

<nav class="main-nav">
  <a style="left:106px;width:70px">HOME</a><span class="divider" style="left:188px"></span>
  <a style="left:188px;width:163px">TUTOR PROFILES</a><span class="divider" style="left:351px"></span>
  <a style="left:351px;width:144px">HOW IT WORKS</a><span class="divider" style="left:495px"></span>
  <a style="left:495px;width:145px">TESTIMONIALS</a><span class="divider" style="left:640px"></span>
  <a style="left:640px;width:95px">PRICES</a><span class="divider" style="left:735px"></span>
  <a style="left:735px;width:125px">CONTACT US</a>
</nav>

<section class="hero">
  <svg width="1200" height="330" viewBox="0 0 1200 330" role="img" aria-label="Photo of a person typing on a laptop, darkened behind the page title">
    <defs>
      <linearGradient id="heroTone" x1="0" y1="0" x2="1" y2="1">
        <stop offset="0" stop-color="#4a4d4a"/>
        <stop offset=".45" stop-color="#5d5452"/>
        <stop offset=".75" stop-color="#3d3f4c"/>
        <stop offset="1" stop-color="#2f3242"/>
      </linearGradient>
    </defs>
    <path d="M0 0H1200V255L600 328L0 255Z" fill="url(#heroTone)"/>
    <polyline points="0,255 600,328 1200,255" fill="none" stroke="#1ba0dc" stroke-width="5"/>
  </svg>
  <h1 class="hero-title">PARENT'S REGISTRATION</h1>
</section>

<form>
  <div class="field" style="left:219px;top:549px">First Name / Last Name</div>
  <div class="field" style="left:613px;top:549px">Address</div>
  <div class="field" style="left:219px;top:600px">Email</div>
  <div class="field" style="left:613px;top:600px">Phone number</div>
  <div class="field add-child" style="left:219px;top:651px">Add Child</div>
  <div class="field" style="left:613px;top:651px">Username <span class="hint">(the email address)</span></div>
  <div class="field" style="left:219px;top:703px">Tick T&amp;Cs</div>
  <div class="field" style="left:613px;top:703px">Create a password</div>
  <div class="register-btn">Register</div>
</form>

<footer class="site-footer">
  <h3 class="footer-heading" style="left:98px">Contact Us</h3>
  <p class="footer-text" style="left:99px;top:75px">Level 3, 42 Harbour Lane, Brisbane<br>QLD 4000, Australia</p>
  <svg class="contact-icon" style="left:101px;top:130px" width="18" height="18" viewBox="0 0 18 18"><path d="M3 1.5l3 3-1.8 2c1 2.5 3.5 5 6.3 6.3l2-1.8 3 3-2 2C7.5 15.5 2.5 10.5 1 3.5z" fill="none" stroke="#fff" stroke-width="1.2"/></svg>
  <p class="footer-text" style="left:135px;top:129px">Phone : +61 7 3000 1842<br>Fax : +61 7 3000 1843</p>
  <svg class="contact-icon" style="left:100px;top:184px" width="20" height="14" viewBox="0 0 20 14"><rect x=".7" y=".7" width="18.6" height="12.6" fill="none" stroke="#fff" stroke-width="1.2"/><path d="M.7 .7L10 8l9.3-7.3M.7 13.3l7-6M19.3 13.3l-7-6" fill="none" stroke="#fff" stroke-width="1.2"/></svg>
  <p class="footer-text" style="left:136px;top:181px">Email: info@brivano.com.au</p>

  <h3 class="footer-heading" style="left:424px">Useful Links</h3>
  <ul class="links">
    <li>Home</li><li>About Us</li><li>Services</li><li>Tutor Profile</li>
    <li>How It Works</li><li>Scheduler</li><li>Testimonials</li><li>Contact Us</li>
  </ul>

  <h3 class="footer-heading" style="left:623px">Join Our Newsletter</h3>
  <p class="news-text">Sed ut perspiciatis unde omnis iste natus error sit voluptatem accusantium doloremque laudantium,</p>
  <div class="news-input">Enter Name</div>
  <div class="news-btn">Subscribe</div>

  <h3 class="footer-heading" style="left:1006px">Social</h3>
  <ul class="social">
    <li><span class="ring"></span>Facepage</li>
    <li><span class="ring"></span>Chirpnet</li>
    <li><span class="ring"></span>Circles+</li>
    <li><span class="ring"></span>vidstream</li>
  </ul>
</footer>

<div class="copyright">Copyright 2016 | All Rights Reserved -- Brivano</div>

</div>
</body>
</html>
```